Website Front Page Slider Graphic

I'm looking for some first impression, artwork/design for teh front page of our website. The image needs to be 1300 x 500 .We sell ID Badge Card Printers, for government, hospital and corporate/ business peoples photo ID security cards. The artwork should be relevant to this - And have a Box / section on the side where we can add heading text and a button. I have attached image of a slider design I like - But this is more for indication of the white box size and position etc. Also attached is some images that are relevant to the products we sell (USING THESE IMAGES IS NOT MANDATORY) We are happy to purchase relevant stock artwork if the winning design has that involved.

our site is cardvantage.com.au the top section on the home page is what this design will be replacing (Above the logos of customers we look after)

Target Market(s)

Government and Security Personnell

Colors
abd036
eaf2ce
5c5c5c
e8e8e8
c4c4c4
0455a3
f37122
ffffff
1b1b1b

Requirements
Must have
• Must have a space for use to include our own text and button. This will be put in as part of our word press slider. The artwork needs to have a section where text could be overlayed and easily visible. (Either dark or light section)
• The design needs to fit in with the look and feel of our site. cardvantage.com.au

```html
<!DOCTYPE html>
<html lang="en">
<head>
<meta charset="utf-8">
<title>ID Card Printers – Front Page Slider</title>
<link rel="stylesheet" href="https://fonts.googleapis.com/css2?family=Open+Sans:wght@400&display=swap">
<style>
  :root {
    --bg-charcoal: #2b2b2d;
    --bg-stripe-dark: #232325;
    --bg-stripe-mid: #3a3a3c;
    --accent-red: #e51b35;
    --accent-red-deep: #b82134;
    --band-navy: #13213d;
    --panel-tint: rgba(255, 255, 255, 0.16);
    --text-light: #ffffff;
    --photo-light: #8c8d90;
    --photo-dark: #4a4b4f;
  }
  * { margin: 0; padding: 0; box-sizing: border-box; }
  html, body { width: 1200px; height: 462px; overflow: hidden; background: var(--bg-charcoal); }
  .slider {
    position: relative;
    width: 1200px;
    height: 462px;
    overflow: hidden;
    background: var(--bg-charcoal);
    font-family: "Open Sans", sans-serif;
  }
  .slider__backdrop { position: absolute; inset: 0; }
  .text-panel {
    position: absolute;
    width: 321px;
    height: 360px;
    background: var(--panel-tint);
  }
  .text-panel--back { left: 94px; top: 48px; }
  .text-panel--front { left: 122px; top: 68px; }
  .text-panel__copy {
    position: absolute;
    left: 131px;
    top: 106px;
    color: var(--text-light);
    font-size: 25px;
    line-height: 29px;
    letter-spacing: 0.3px;
  }
  .text-panel__group { margin-bottom: 30px; }
  .text-panel__line--indent { padding-left: 27px; }
  .slide-nav {
    position: absolute;
    left: 83px;
    top: 206px;
    width: 54px;
    height: 54px;
    border-radius: 50%;
    background: rgba(184, 33, 52, 0.75);
  }
  .slide-nav svg { display: block; }
</style>
</head>
<body>
<main class="slider">
  <svg class="slider__backdrop" width="1200" height="462" viewBox="0 0 1200 462" aria-hidden="false">
    <defs>
      <linearGradient id="photoTone" x1="0" y1="0" x2="1" y2="1">
        <stop offset="0" stop-color="var(--photo-light)"/>
        <stop offset="0.55" stop-color="#7a7b7e"/>
        <stop offset="1" stop-color="var(--photo-dark)"/>
      </linearGradient>
      <linearGradient id="navyBand" x1="0" y1="0" x2="0" y2="1">
        <stop offset="0" stop-color="#132342"/>
        <stop offset="1" stop-color="#0f1b33"/>
      </linearGradient>
      <linearGradient id="redStripe" x1="0" y1="0" x2="0" y2="1">
        <stop offset="0" stop-color="#e8142f"/>
        <stop offset="1" stop-color="#c91d36"/>
      </linearGradient>
    </defs>
    <!-- backdrop diagonal stripes -->
    <polygon points="0,0 150,0 0,280" fill="var(--bg-stripe-mid)" opacity="0.55"/>
    <polygon points="150,0 250,0 0,462 0,280" fill="var(--bg-stripe-dark)" opacity="0.7"/>
    <polygon points="300,0 380,0 130,462 50,462" fill="var(--bg-stripe-mid)" opacity="0.5"/>
    <polygon points="320,0 470,0 230,462 80,462" fill="var(--accent-red-deep)" opacity="0.35"/>
    <polygon points="470,0 560,0 310,462 230,462" fill="var(--bg-stripe-dark)" opacity="0.8"/>
    <!-- navy band -->
    <polygon points="572,0 798,0 545,462 318,462" fill="url(#navyBand)"/>
    <!-- red stripe -->
    <polygon points="794,0 873,0 628,462 540,462" fill="url(#redStripe)"/>
    <!-- photo area -->
    <polygon role="img" aria-label="Photo: receptionist at a front desk using a desktop ID card printer beside a computer monitor"
             points="873,0 1200,0 1200,462 628,462" fill="url(#photoTone)"/>
    <polygon points="873,0 1200,0 1200,462 628,462" fill="#000" opacity="0.25"/>
  </svg>

  <div class="text-panel text-panel--back"></div>
  <div class="text-panel text-panel--front"></div>

  <div class="text-panel__copy">
    <p class="text-panel__group">
      <span class="text-panel__line">add yourtext here</span><br>
      <span class="text-panel__line text-panel__line--indent">add yourtext here</span>
    </p>
    <p class="text-panel__group">
      <span class="text-panel__line">add yourtext here</span><br>
      <span class="text-panel__line text-panel__line--indent">add yourtext here</span>
    </p>
    <p class="text-panel__group">
      <span class="text-panel__line">add yourtext here</span><br>
      <span class="text-panel__line text-panel__line--indent">add yourtext here</span>
    </p>
  </div>

  <div class="slide-nav" aria-label="Previous slide">
    <svg width="54" height="54" viewBox="0 0 54 54">
      <polyline points="26,16 16,27 26,38" fill="none" stroke="#fff" stroke-width="5" stroke-linecap="round" stroke-linejoin="round"/>
      <polyline points="37,16 27,27 37,38" fill="none" stroke="#fff" stroke-width="5" stroke-linecap="round" stroke-linejoin="round"/>
    </svg>
  </div>
</main>
</body>
</html>
```